Criação de Power Point Slide Mestre para Consultoria de Negócios
A empresa queria:
" É uma empresa de consultoria no ramo de desenvolvimento de software estatístico e de modelos de séries temporais (por favor, ler folder em anexo). "

```html
<!DOCTYPE html>
<html lang="pt-BR">
<head>
<meta charset="UTF-8">
<title>Diferencial — Slide Mestre</title>
<link rel="stylesheet" href="https://fonts.googleapis.com/css2?family=Open+Sans:wght@400;600&family=Nunito:wght@600&display=swap">
<style>
  :root {
    --page-bg: #e6e9ec;
    --slide-bg: #ffffff;
    --navy: #1d4a66;
    --teal: #2b6d80;
    --green: #3a9f57;
    --text: #4f5559;
    --icon-orange: #e0773a;
    --icon-blue: #2f6f9a;
    --icon-teal: #3c8b93;
  }
  * { box-sizing: border-box; margin: 0; padding: 0; }
  html, body { width: 1200px; height: 1200px; overflow: hidden; }
  body { background: var(--page-bg); position: relative; font-family: "Open Sans", sans-serif; }

  .slide {
    position: absolute; left: 50px; top: 290px;
    width: 1100px; height: 620px;
    background: var(--slide-bg);
    overflow: hidden;
    box-shadow: 0 6px 24px rgba(0,0,0,0.12);
  }
  .slide-corner { position: absolute; inset: 0; }

  .title-tab {
    position: absolute; left: 60px; top: 42px;
    width: 330px; height: 60px;
    background: var(--teal);
    border-radius: 10px 10px 10px 0;
    color: #fff;
    font-family: "Nunito", sans-serif; font-weight: 600;
    font-size: 34px; line-height: 60px; padding-left: 24px;
  }
  .title-rule {
    position: absolute; left: 60px; top: 104px;
    width: 640px; height: 2px; background: var(--teal); opacity: 0.5;
  }

  .icon {
    position: absolute; width: 72px; height: 72px; border-radius: 50%;
  }
  .icon-target { left: 92px; top: 140px; background: var(--icon-orange); }
  .icon-team { left: 70px; top: 370px; background: var(--icon-blue); }
  .icon-chart { left: 700px; top: 360px; background: var(--icon-teal); }

  .body-text {
    position: absolute; color: var(--text);
    font-size: 19px; line-height: 1.5; text-align: justify;
  }
  .text-clients { left: 190px; top: 140px; width: 520px; }
  .text-method { left: 60px; top: 252px; width: 630px; }
  .text-team { left: 170px; top: 370px; width: 500px; }

  .brand {
    position: absolute; right: 70px; bottom: 44px;
    display: flex; align-items: center; gap: 14px;
    font-family: "Open Sans", sans-serif; font-weight: 600;
    font-size: 40px; color: var(--teal);
  }
  .brand-dot { width: 40px; height: 40px; border-radius: 50%; background: var(--green); }
</style>
</head>
<body>
  <section class="slide">
    <svg class="slide-corner" viewBox="0 0 1100 620" width="1100" height="620" aria-hidden="true">
      <path d="M690 0 Q1010 40 1100 330 L1100 0 Z" fill="var(--navy)"/>
      <path d="M660 0 Q1000 36 1100 360" fill="none" stroke="var(--green)" stroke-width="10"/>
      <path d="M640 0 Q990 34 1100 385" fill="none" stroke="var(--teal)" stroke-width="3" opacity="0.6"/>
    </svg>

    <h1 class="title-tab">Diferencial</h1>
    <div class="title-rule"></div>

    <div class="icon icon-target" role="img" aria-label="Ícone de alvo"></div>
    <p class="body-text text-clients">Atendemos empresas de pequeno, médio e grande porte, fornecendo além das informações demandadas, plataformas capazes de produzir tais estudos.</p>

    <p class="body-text text-method">Somos pragmáticos e abertos a novas soluções. Começamos por definir as questões certas, para então analisá-las com rigor analítico, como base para criar soluções.</p>

    <div class="icon icon-team" role="img" aria-label="Ícone de equipe e ideias"></div>
    <p class="body-text text-team">Nossa equipe, formada por mestres e doutores, possui forte vínculo com a academia, buscando sempre trazer conhecimentos de fronteira para nossos clientes.</p>

    <div class="icon icon-chart" role="img" aria-label="Ícone de gráfico"></div>

    <div class="brand"><span class="brand-dot"></span>Veltora</div>
  </section>
</body>
</html>
```